Wedding Invitation to be used digitally

Design of a Wedding Invitation.
It will be used digitally by whatsapp, so the file format and image size should be appropriate. We don´t intend to print.
Word file with the text contents as attachment. This is REALLY just the text and the main sequencial order of the information that should appear in the invitation.
However, ALL criativity is welcome ofcourse in terms of organization of the information in the paper, font, uppercase and lowercase, numbers and their format, dates and their format, drawings, logo, etc etc

Target Market(s)

family and friends

Requirements
Must have
• A logo at the top with the capitals of our name - R and T
Nice to have
• Should be elegant

```html
<!DOCTYPE html>
<html lang="en">
<head>
<meta charset="utf-8">
<title>Renata &amp; Tiago — Wedding Invitation</title>
<link rel="stylesheet" href="https://fonts.googleapis.com/css2?family=Quicksand:wght@400;500;700&display=swap">
<style>
  :root {
    --page-bg: #efeeef;
    --marble-dark: #2e3033;
    --marble-mid: #4a4c52;
    --marble-blue: #3a4150;
    --panel: #282724;
    --gold: #e2b45f;
    --gold-light: #f1d98c;
    --gold-frame: #d9a444;
    --ink-light: #f4f1ea;
  }
  * { margin: 0; padding: 0; box-sizing: border-box; }
  html, body {
    width: 1200px; height: 1200px; overflow: hidden;
    background: var(--page-bg);
    font-family: "Quicksand", sans-serif;
  }
  .invitation {
    position: absolute; left: 296px; top: 60px;
    width: 608px; height: 1080px;
  }
  .marble-backdrop {
    position: absolute; inset: 0;
    background:
      radial-gradient(ellipse at 80% 10%, var(--marble-blue) 0%, transparent 55%),
      radial-gradient(ellipse at 15% 90%, var(--marble-mid) 0%, transparent 60%),
      linear-gradient(160deg, var(--marble-mid) 0%, var(--marble-dark) 50%, var(--marble-blue) 100%);
  }
  .content-panel {
    position: absolute; left: 31px; top: 97px;
    width: 549px; height: 894px;
    background: var(--panel);
    border: 2px solid var(--gold-frame);
  }
  .line {
    position: absolute; left: 0; right: 0;
    text-align: center; transform: translateY(-50%);
    color: var(--ink-light); font-size: 18px; font-weight: 400;
    white-space: nowrap;
  }
  .monogram {
    color: var(--gold); font-size: 100px; font-weight: 700;
    letter-spacing: 6px; line-height: 1;
  }
  .couple-name { color: var(--gold); font-size: 27px; font-weight: 700; }
  .ampersand { color: var(--gold); font-size: 24px; }
  .line.small { font-size: 17px; }
  .divider { position: absolute; left: 50%; transform: translate(-50%, -50%); }
</style>
</head>
<body>
  <main class="invitation">
    <div class="marble-backdrop" role="img" aria-label="Dark grey and blue marble texture with gold veins"></div>

    <section class="content-panel">
      <div class="line monogram" style="top:121px">RT</div>

      <p class="line" style="top:277px">Together with their families</p>
      <h1 class="line couple-name" style="top:322px">Renata Vale</h1>
      <p class="line ampersand" style="top:368px">&amp;</p>
      <h1 class="line couple-name" style="top:411px">Tiago Moreira</h1>
      <p class="line" style="top:459px">Invite you to their Wedding Celebration</p>

      <svg class="divider" style="top:488px" width="104" height="6" viewBox="0 0 104 6" aria-hidden="true">
        <g fill="var(--gold)"><circle cx="3" cy="3" r="2"/><circle cx="14" cy="3" r="2"/><circle cx="25" cy="3" r="2"/><circle cx="36" cy="3" r="2"/><circle cx="47" cy="3" r="2"/><circle cx="58" cy="3" r="2"/><circle cx="69" cy="3" r="2"/><circle cx="80" cy="3" r="2"/><circle cx="91" cy="3" r="2"/><circle cx="101" cy="3" r="2"/></g>
      </svg>

      <p class="line" style="top:519px">Sunday, July 28, 2024</p>
      <p class="line" style="top:551px">At 11H30</p>

      <svg class="divider" style="top:581px" width="104" height="6" viewBox="0 0 104 6" aria-hidden="true">
        <g fill="var(--gold)"><circle cx="3" cy="3" r="2"/><circle cx="14" cy="3" r="2"/><circle cx="25" cy="3" r="2"/><circle cx="36" cy="3" r="2"/><circle cx="47" cy="3" r="2"/><circle cx="58" cy="3" r="2"/><circle cx="69" cy="3" r="2"/><circle cx="80" cy="3" r="2"/><circle cx="91" cy="3" r="2"/><circle cx="101" cy="3" r="2"/></g>
      </svg>

      <p class="line" style="top:610px">Capela de Santa Luzia | Vila do Mar</p>
      <p class="line small" style="top:645px">(Parking – Marina do Porto Velho or Parque Terra Velha)</p>

      <svg class="divider" style="top:672px" width="104" height="6" viewBox="0 0 104 6" aria-hidden="true">
        <g fill="var(--gold)"><circle cx="3" cy="3" r="2"/><circle cx="14" cy="3" r="2"/><circle cx="25" cy="3" r="2"/><circle cx="36" cy="3" r="2"/><circle cx="47" cy="3" r="2"/><circle cx="58" cy="3" r="2"/><circle cx="69" cy="3" r="2"/><circle cx="80" cy="3" r="2"/><circle cx="91" cy="3" r="2"/><circle cx="101" cy="3" r="2"/></g>
      </svg>

      <p class="line" style="top:699px">Reception to Follow</p>
      <p class="line" style="top:731px">At</p>
      <p class="line" style="top:764px">Hotel Forte da Areia | Vila do Mar</p>
      <p class="line" style="top:798px">(Parking – on site)</p>

      <svg class="divider" style="top:826px" width="104" height="6" viewBox="0 0 104 6" aria-hidden="true">
        <g fill="var(--gold)"><circle cx="3" cy="3" r="2"/><circle cx="14" cy="3" r="2"/><circle cx="25" cy="3" r="2"/><circle cx="36" cy="3" r="2"/><circle cx="47" cy="3" r="2"/><circle cx="58" cy="3" r="2"/><circle cx="69" cy="3" r="2"/><circle cx="80" cy="3" r="2"/><circle cx="91" cy="3" r="2"/><circle cx="101" cy="3" r="2"/></g>
      </svg>

      <p class="line" style="top:855px">RSVP by 20th July</p>
    </section>
  </main>
</body>
</html>
```